Web Design Project

Parallel Press owns and operates a large number of editorial websites. These websites provides mostly consumers in the financial services space with information and price comparisons for a particular service.

Parallel Press, as the holding company for each of these sites, currently has no website. We need to build a website targeted towards potential partners for our websites. The idea being that when we start a conversation with a partner, they can view our site and obtain some basic information about who we are.

The structure of the site is to be very simple, containing only a brief description about who we are, our contact details and a list of some of our websites:
• LifeCoverHub.net.au
• MotorCoverCheckers.com.au
• HouseCoverCheckers.com.au
• MedicalCoverCheckers.com.au
• LivingCoverCheckers.com.au
• TripCoverCheckers.com.au
• AnimalCoverCheckers.com.au
• PrivateCreditCheckers.com.au
• MobileCoolingUnit.com.au
• FixedSavingYield.com.au
• ThriftyDays.com.au
• CashNana.com.au
• TameThePlastic.com.au
• PurseKeeper.com.au
• ThirdPartyClaimsCoverOz.com.au
• Trade-Protection.com.au
• MotorCoverProviders.com.au
• MedicalCoverProviders.com.au
• HouseCoverDownUnder.com
• LivingCoverDownUnder.com
• SalaryShieldCoverDownUnder.com
• MedicalCoverDownUnder.com
• AnimalCoverDownUnder.com
• PrivateCreditDownUnder.com
• PlasticPaysDownUnder.com
• HouseFinanceDownUnder.com
• RetireFundHub.net.au

The design of the site should say 'Internet company', 'professional', 'fresh thinking'. The design should not look like a corporate site that you would see from any corporate services business with images of people in suits. We are ultimately an Internet business and there should be a unique feel to the site.

We are open to a suggestion of a colour pallet as the holding company does not have an established logo.

Some sites that we like are:

http://www.brindle-studio.example/#home
http://preview11.layoutvault.example/wt_48261/index.html
http://preview11.layoutvault.example/wordpress_59134/
http://mulloptic.example/
http://www.tandrel.example/
http://www.kovasilindqvist.example/
http://www.sharpsitegallery.example/Corporate/design-ideas-detail.html?id=4172
http://brackenway.example/
http://oskarteel.example/

Reason: Hi all, Apologies, but I need to extend the timeline. One of our key stakeholders is away for the next week. There are a few good designs that we have received to date and there are some tweaks that we would like to see before making a final decision. Thank you to everyone that has submitted designs - Have a great new year. Bram

Reason: Sorry to have to delay the deadline on this, but we did not find anything in the designs really resonated with us. We will have a further think about the existing designs that have been submitted and how we can provide more specific feedback to the designers to make some modifications to the designs.

Target Market(s)

We are targeting insurance companies / brokers that we are talking to. The idea is that we show a professional face to them.

Industry/Entity Type

Financial

Requirements
Must have
• Home Page (possibly integrated with About us details)
Contact Us
Our Sites

```html
<!DOCTYPE html>
<html lang="en">
<head>
<meta charset="utf-8">
<title>Parallel Press</title>
<link rel="stylesheet" href="https://fonts.googleapis.com/css2?family=Quicksand:wght@400;500;700&display=swap">
<style>
  :root {
    --sky: #0a5274;
    --sky-deep: #084766;
    --band: #0b4566;
    --band-deep: #093c5b;
    --footer: #0f2232;
    --footer-deep: #0c1b28;
    --orange: #f7a521;
    --orange-light: #fbb53a;
    --white: #ffffff;
    --link: #1f6f9a;
  }
  * { margin: 0; padding: 0; box-sizing: border-box; }
  html, body { width: 1200px; height: 797px; overflow: hidden; }
  body {
    position: relative;
    font-family: "Quicksand", sans-serif;
    background: radial-gradient(ellipse at 55% 35%, var(--sky) 0%, var(--sky-deep) 100%);
  }
  .brand {
    position: absolute; left: 323px; top: 37px;
    display: flex; align-items: center; gap: 10px;
  }
  .brand-dot {
    width: 56px; height: 56px; border-radius: 50%;
    background: radial-gradient(circle at 40% 35%, var(--orange-light), var(--orange));
  }
  .brand-name {
    font-size: 25px; font-weight: 500; color: var(--orange); letter-spacing: 0.2px;
  }
  .actions { position: absolute; left: 0; top: 0; width: 1200px; height: 478px; }
  .action {
    position: absolute; top: 191px; width: 208px; height: 208px; border-radius: 50%;
    background: var(--orange);
    display: flex; align-items: center; justify-content: center;
    color: var(--white); font-size: 26px; font-weight: 400; text-decoration: none;
    padding-top: 4px;
  }
  .action::after {
    content: ""; position: absolute; left: 14px; right: 14px; bottom: -12px; height: 14px;
    border-radius: 50%; background: rgba(0, 25, 40, 0.35); filter: blur(5px); z-index: -1;
  }
  .action-contact { left: 380px; }
  .action-sites { left: 615px; }
  .about {
    position: absolute; left: 0; top: 478px; width: 1200px; height: 168px;
    background: linear-gradient(180deg, var(--band) 0%, var(--band-deep) 100%);
  }
  .about-text {
    position: absolute; left: 350px; top: 32px; width: 499px;
    color: var(--white); font-size: 17px; line-height: 21px; letter-spacing: 1.6px;
    text-align: justify; font-weight: 400;
  }
  .about-arrow { position: absolute; top: 66px; width: 12px; height: 20px; }
  .about-arrow-prev { left: 318px; }
  .about-arrow-next { left: 876px; }
  .footer {
    position: absolute; left: 0; top: 646px; width: 1200px; height: 151px;
    background: linear-gradient(180deg, var(--footer) 0%, var(--footer-deep) 100%);
    font-family: Arial, Helvetica, sans-serif;
  }
  .footer-nav { position: absolute; left: 365px; top: 28px; display: flex; gap: 16px; }
  .footer-nav a { color: var(--link); font-size: 9px; font-weight: 700; text-decoration: none; }
  .footer-copy { position: absolute; left: 364px; top: 60px; color: var(--link); font-size: 8px; }
</style>
</head>
<body>
  <header class="brand">
    <span class="brand-dot"></span>
    <span class="brand-name">parallel press</span>
  </header>

  <nav class="actions">
    <a class="action action-contact" href="#contact">Contact Us</a>
    <a class="action action-sites" href="#sites">Our Sites</a>
  </nav>

  <section class="about">
    <svg class="about-arrow about-arrow-prev" viewBox="0 0 12 20" aria-label="Previous">
      <polyline points="10,2 2,10 10,18" fill="none" stroke="#f7a521" stroke-width="1.6"/>
    </svg>
    <p class="about-text">Parallel Press owns and operates a large number of editorial websites. These websites provides mostly consumers in the financial services space with information and price comparisons for a particular service</p>
    <svg class="about-arrow about-arrow-next" viewBox="0 0 12 20" aria-label="Next">
      <polyline points="2,2 10,10 2,18" fill="none" stroke="#f7a521" stroke-width="1.6"/>
    </svg>
  </section>

  <footer class="footer">
    <nav class="footer-nav">
      <a href="#about">About Us</a>
      <a href="#contact">Contact Us</a>
      <a href="#sites">Our Sites</a>
    </nav>
    <p class="footer-copy">&copy; parallel press, all rights reserved, 2012</p>
  </footer>
</body>
</html>
```